Powerpoint Design for AI Consulting Company

Description
Falcon Reed Industries is a consulting and technology company that engineers AI transformations, automation, and decision intelligence for financial firms, mining companies, and supply chains.
We already have a logo and brand colors (see attached). We need a professional, modern PowerPoint template that reflects our brand identity and positioning.
Key Requirements
Use our logo and color palette (deep blue, orange, white/black backgrounds).
Clean, modern design with subtle technology-inspired elements (data flows, AI networks, abstract systems).
Must feel sophisticated, bold, and boardroom-ready for executive presentations.
Templates should support both dark and light backgrounds.
Deliverables
A reusable PowerPoint template (.PPTX) with at least these layouts:
Title / Cover slide – dramatic, logo placement, tagline space.
Agenda slide – clean, structured layout.
Section divider slides – strong use of brand colors.
Content slides – text + image, text + icon.
Charts & data slides – bar, line, pie, comparison table, infographics.
Case study / example project slide. - ROI / Transformation Journey
Timeline / roadmap slide.
Team profile slide.
Reframe Slide – A provocative insight that reframes the client’s current thinking.
Options & Trade-offs Slide – Matrix showing different paths and consequences.
Execution Roadmap Slide – Step-by-step phased implementation view.
Closing / thank-you slide with contact details.
Style Guide
Colors: Primary – deep blue (#0D3559), Secondary – orange (#E87722), Accents – silver/white.
Fonts: Modern sans-serif (e.g., Montserrat, Lato, or similar).
Visual elements: Abstract technology, data-inspired graphics, mathematical motifs. Avoid clutter or overly “sci-fi” looks.
Tone: Premium consulting + innovative AI firm.
Target Market(s)
Falcon Reed Industries’ target market is senior decision-makers in finance, mining, and supply chains, where complexity, risk, and ROI pressure are high. Primary buyers include family offices, boutique wealth managers, super funds, and mining/supply chain executives, who value insight-driven strategies, automation, and decision intelligence. A secondary market includes professional services (accounting, legal, medical) and regulated SMEs (daycare, aged care, community services) burdened by admin and compliance. The slide deck must appeal to a boardroom audience — authoritative, data-driven, and visually clean — while remaining flexible enough to adapt for SME professional services.
Look and feel
Each slider illustrates characteristics of the customer's brand and the style your logo design should communicate.

```html
<!DOCTYPE html>
<html lang="en">
<head>
<meta charset="utf-8">
<title>Falcon Reed Industries – Presentation Template</title>
<link href="https://fonts.googleapis.com/css2?family=Inter:wght@300;400;500;600;700;800&display=swap" rel="stylesheet">
<style>
:root{
  --canvas:#c9cacd;
  --navy:#0d3559;
  --navy-deep:#0a2443;
  --ink:#0b1733;
  --blue-text:#1b3a7a;
  --orange:#e8671e;
  --white:#ffffff;
  --silver:#eef0f4;
  --grey-text:#3a3f4a;
  --line:#b9c6dc;
}
*{margin:0;padding:0;box-sizing:border-box}
html,body{width:1031px;height:1200px;overflow:hidden}
body{background:var(--canvas);font-family:"Inter",Arial,sans-serif;position:relative;color:var(--grey-text)}
.slide{position:absolute;width:440px;height:247px;overflow:hidden;background:var(--white)}
.slide.dark{background:var(--navy-deep);color:var(--white)}
.abs{position:absolute}
.network{position:absolute;top:0;right:0;width:300px;height:60px;background:linear-gradient(90deg,rgba(255,255,255,0),rgba(214,220,232,.55) 40%,rgba(236,239,245,.3))}
.slide-title{position:absolute;left:18px;top:18px;font-size:15.5px;font-weight:500;color:var(--blue-text);white-space:nowrap}
.slide-title .accent{color:var(--orange)}
.title-rule{position:absolute;left:16px;height:1.5px;background:var(--blue-text)}

/* cover */
.cover{left:62px;top:64px;background:radial-gradient(ellipse at 50% 0%,#1d2a6b 0%,#070b2c 45%,#02040f 100%)}
.cover .wave{left:0;right:0;bottom:0;height:110px;background:radial-gradient(ellipse at 50% 70%,rgba(32,150,150,.45),rgba(10,40,60,0) 70%)}
.brand-lockup{left:0;right:0;top:30px;text-align:center}
.brand-name{font-weight:700;font-size:15px;letter-spacing:.5px;color:#2a5aa8;line-height:1.1}
.brand-tag{font-size:7px;font-weight:600;letter-spacing:.6px;color:#2a5aa8;margin-top:2px}
.cover-title{left:0;right:0;top:103px;text-align:center;font-size:21px;font-weight:800;letter-spacing:.2px}
.cover-title .accent{color:var(--orange)}
.cover-sub{left:0;right:0;top:134px;text-align:center;font-size:14px;font-weight:300}

/* agenda */
.agenda{left:530px;top:64px;border-top:3px solid var(--orange)}
.agenda-list{left:12px;top:58px;width:410px;list-style:none}
.agenda-list li{display:flex;justify-content:space-between;align-items:center;height:26.3px;border-bottom:1.5px solid var(--navy);font-size:8.6px;color:var(--blue-text);padding:0 14px 0 20px;position:relative}
.agenda-list li:last-child{border-bottom:none}
.agenda-list li::before{content:"";position:absolute;left:9px;width:4px;height:4px;border-radius:50%;background:var(--blue-text)}

/* divider */
.divider{left:61px;top:344px;background:radial-gradient(ellipse at 60% 40%,#16386b 0%,#0c2a55 55%,#0a2146 100%)}
.divider .rule{left:53px;width:333px;height:1.5px;background:var(--orange)}
.divider-title{left:53px;top:104px;font-size:23px;font-weight:300}

/* content */
.content{left:530px;top:344px}
.bullets{left:22px;top:69px;width:180px;list-style:none}
.bullets li{font-size:8.4px;line-height:13.5px;color:#1d2230;padding-left:16px;position:relative;margin-bottom:14px}
.bullets li::before{content:"";position:absolute;left:0;top:4px;width:5px;height:5px;border-radius:50%;background:var(--orange)}
.photo{left:211px;top:59px;width:215px;height:168px;border-radius:8px;background:linear-gradient(135deg,#0c2540,#1f5f86 55%,#0b1d33)}

/* capabilities */
.caps{left:62px;top:620px}
.cap-card{top:59px;width:126px;height:174px;background:var(--navy);border-radius:5px;text-align:center;color:var(--white)}
.cap-icon{width:45px;height:45px;margin:20px auto 0;border:1.5px solid var(--orange);border-radius:50%;display:flex;align-items:center;justify-content:center}
.cap-name{font-size:9px;font-weight:700;margin-top:18px}
.cap-text{font-size:5.6px;line-height:8.3px;padding:0 10px;margin-top:7px;color:#e3e8f0}

/* roadmap */
.roadmap{left:530px;top:620px}
.phase-arc{top:63px;width:80px;height:48px;border:1.3px solid var(--orange);border-bottom:none;border-radius:40px 40px 0 0;display:flex;justify-content:center;padding-top:12px}
.phase-bar{top:109px;height:26px;background:var(--navy);color:var(--white);font-size:11px;display:flex;align-items:center;justify-content:center;clip-path:polygon(0 0,92% 0,100% 50%,92% 100%,0 100%)}
.phase-col{top:150px;width:100px;text-align:center}
.pill{display:inline-block;font-size:5.6px;background:var(--silver);border-radius:6px;padding:3px 7px;color:#1d2230}
.phase-name{font-size:7px;font-weight:700;color:#1d2230;margin-top:6px}
.phase-text{font-size:4.8px;line-height:6.9px;margin-top:4px;color:#333}
.col-sep{top:148px;width:1px;height:88px;background:#d9dde5}

/* leadership */
.leaders{left:62px;top:895px}
.leader{top:50px;width:100px;height:188px;border:1px solid var(--line);border-top:none;border-radius:0 0 48px 48px;text-align:center}
.portrait{width:83px;height:83px;border-radius:50%;margin:6px auto 0;background:linear-gradient(160deg,#d7d9dd,#5a6b85 70%,#1c2a45)}
.leader-name{font-size:7.5px;font-weight:600;color:var(--blue-text);margin-top:9px}
.leader-role{font-size:5.8px;color:#1d2230;margin-top:3px}
.leader-bio{font-size:4.9px;line-height:6.9px;padding:0 12px;margin-top:7px;color:#333}

/* closing */
.closing{left:530px;top:896px;background:radial-gradient(ellipse at 50% 50%,#173768,#0c2550 70%,#0a2046)}
.closing .brand-name,.closing .brand-tag{color:var(--orange)}
.thanks{left:0;right:0;top:98px;text-align:center;font-size:40px;font-weight:500}
.contact{left:0;right:0;text-align:center;font-size:10px;font-weight:300;display:flex;justify-content:center;align-items:center;gap:6px}
</style>
</head>
<body>

<!-- Cover -->
<section class="slide dark cover">
  <div class="abs wave" role="img" aria-label="Abstract teal particle wave"></div>
  <div class="abs brand-lockup">
    <div class="brand-name">FALCON REED INDUSTRIES</div>
    <div class="brand-tag">Engineering AI Transformations</div>
  </div>
  <h1 class="abs cover-title">FALCON REED <span class="accent">INDUSTRIES</span></h1>
  <p class="abs cover-sub">Engineering AI Transformation</p>
</section>

<!-- Agenda -->
<section class="slide agenda">
  <div class="network" role="img" aria-label="Faint data network pattern"></div>
  <h2 class="slide-title" style="top:16px">Agenda</h2>
  <div class="title-rule" style="top:43px;width:65px;left:12px"></div>
  <ul class="abs agenda-list">
    <li><span>Who We Are</span><span>2</span></li>
    <li><span>The AI Transformation Imperative</span><span>3</span></li>
    <li><span>Our Solutions &amp; Approach</span><span>4</span></li>
    <li><span>Case Studies &amp; ROI</span><span>5</span></li>
    <li><span>Execution Roadmap</span><span>6</span></li>
    <li><span>Options &amp; Trade-Offs</span><span>7</span></li>
    <li><span>Next Steps</span><span>8</span></li>
  </ul>
</section>

<!-- Section divider -->
<section class="slide dark divider">
  <div class="abs rule" style="top:89px"></div>
  <h2 class="abs divider-title">The AI Transformation Imperative</h2>
  <div class="abs rule" style="top:146px"></div>
</section>

<!-- Text + image -->
<section class="slide content">
  <div class="network" role="img" aria-label="Faint data network pattern"></div>
  <h2 class="slide-title" style="top:13px">AI-Driven Competitive <span class="accent">Advantage</span></h2>
  <div class="title-rule" style="top:41px;width:250px;left:17px"></div>
  <ul class="abs bullets">
    <li>Automate critical decisions at scale</li>
    <li>Reduce operational risk in financial and industrial systems</li>
    <li>Unlock hidden efficiency in supply chains and mining operations</li>
    <li>Drive measurable ROI from AI adoption</li>
  </ul>
  <div class="abs photo" role="img" aria-label="Photo of a humanoid robot and a professional working on a laptop"></div>
</section>

<!-- Capabilities -->
<section class="slide caps">
  <div class="network" role="img" aria-label="Faint data network pattern"></div>
  <h2 class="slide-title" style="top:14px">Our Core <span class="accent">Capabilities</span></h2>
  <div class="title-rule" style="top:42px;width:165px"></div>
  <article class="abs cap-card" style="left:15px">
    <div class="cap-icon"><svg width="22" height="22" viewBox="0 0 22 22"><circle cx="11" cy="11" r="8" fill="none" stroke="#e8671e" stroke-width="2"/><path d="M7 11h8M11 7v8" stroke="#e8671e" stroke-width="2"/></svg></div>
    <h3 class="cap-name">AI Consulting</h3>
    <p class="cap-text">Lorem ipsum dolor sit amet, consectetur adipiscing elit, sed do eiusmod tempor incididunt ut labore et dolore magna aliqua. Ut enim ad minim veniam, quis nostrud exercitation ullamco laboris nisi ut aliquip ex ea commodo.</p>
  </article>
  <article class="abs cap-card" style="left:157px">
    <div class="cap-icon"><svg width="22" height="22" viewBox="0 0 22 22"><circle cx="8" cy="8" r="4" fill="none" stroke="#e8671e" stroke-width="2"/><circle cx="15" cy="15" r="4" fill="none" stroke="#e8671e" stroke-width="2"/></svg></div>
    <h3 class="cap-name">Automation Engineering</h3>
    <p class="cap-text">Lorem ipsum dolor sit amet, consectetur adipiscing elit, sed do eiusmod tempor incididunt ut labore et dolore magna aliqua. Ut enim ad minim veniam, quis nostrud exercitation ullamco laboris nisi ut aliquip ex ea commodo.</p>
  </article>
  <article class="abs cap-card" style="left:297px">
    <div class="cap-icon"><svg width="22" height="22" viewBox="0 0 22 22"><path d="M11 3v16M5 8l6 3 6-3M5 14l6 3 6-3" fill="none" stroke="#e8671e" stroke-width="2"/></svg></div>
    <h3 class="cap-name">Decision Intelligence</h3>
    <p class="cap-text">Lorem ipsum dolor sit amet, consectetur adipiscing elit, sed do eiusmod tempor incididunt ut labore et dolore magna aliqua. Ut enim ad minim veniam, quis nostrud exercitation ullamco laboris nisi ut aliquip ex ea commodo.</p>
  </article>
</section>

<!-- Roadmap -->
<section class="slide roadmap">
  <div class="network" role="img" aria-label="Faint data network pattern"></div>
  <h2 class="slide-title" style="top:14px">AI Transformation <span class="accent">Roadmap</span></h2>
  <div class="title-rule" style="top:42px;width:205px"></div>

  <div class="abs phase-arc" style="left:24px"><svg width="22" height="22" viewBox="0 0 22 22"><circle cx="11" cy="11" r="9" fill="none" stroke="#e8671e" stroke-width="1.8"/><circle cx="11" cy="11" r="4.5" fill="none" stroke="#e8671e" stroke-width="1.8"/><circle cx="11" cy="11" r="1.3" fill="#e8671e"/></svg></div>
  <div class="abs phase-arc" style="left:130px"><svg width="22" height="22" viewBox="0 0 22 22"><rect x="4" y="3" width="12" height="16" rx="1" fill="none" stroke="#e8671e" stroke-width="1.8"/><path d="M7 8h6M7 12h6" stroke="#e8671e" stroke-width="1.8"/></svg></div>
  <div class="abs phase-arc" style="left:236px"><svg width="22" height="22" viewBox="0 0 22 22"><path d="M4 18V12M9 18V7M14 18V10M19 18V4" stroke="#e8671e" stroke-width="2"/></svg></div>
  <div class="abs phase-arc" style="left:339px"><svg width="22" height="22" viewBox="0 0 22 22"><circle cx="11" cy="11" r="8" fill="none" stroke="#e8671e" stroke-width="1.8"/><path d="M6 14l4-4 3 3 4-5" fill="none" stroke="#e8671e" stroke-width="1.8"/></svg></div>

  <div class="abs phase-bar" style="left:18px;width:100px">Phase 1</div>
  <div class="abs phase-bar" style="left:126px;width:100px">Phase 2</div>
  <div class="abs phase-bar" style="left:232px;width:100px">Phase 3</div>
  <div class="abs phase-bar" style="left:335px;width:90px">Phase 4</div>

  <div class="abs col-sep" style="left:118px"></div>
  <div class="abs col-sep" style="left:224px"></div>
  <div class="abs col-sep" style="left:326px"></div>

  <div class="abs phase-col" style="left:16px"><span class="pill">0–3 months</span><h3 class="phase-name">Assessment &amp; Strategy</h3><p class="phase-text">Lorem ipsum dolor sit amet, consectetur adipiscing elit, sed do eiusmod tempor incididunt ut labore et dolore magna aliqua. Ut enim ad minim veniam, quis nostrud exercitation ullamcosint occaecat cupidatat non proident, sunt in culpa qui officia deserunt.</p></div>
  <div class="abs phase-col" style="left:122px"><span class="pill">3–6 months</span><h3 class="phase-name">Pilot &amp; Prototype</h3><p class="phase-text">Lorem ipsum dolor sit amet, consectetur adipiscing elit, sed do eiusmod tempor incididunt ut labore et dolore magna aliqua. Ut enim ad minim veniam, quis nostrud exercitation ullamcosint occaecat cupidatat non proident, sunt in culpa qui officia</p></div>
  <div class="abs phase-col" style="left:226px"><span class="pill">6–12 months</span><h3 class="phase-name">Scale AI Systems</h3><p class="phase-text">Lorem ipsum dolor sit amet, consectetur adipiscing elit, sed do eiusmod tempor incididunt ut labore et dolore magna aliqua. Ut enim ad minim veniam, quis nostrud exercitation ullamcosint occaecat cupidatat non proident, sunt in culpa</p></div>
  <div class="abs phase-col" style="left:326px"><span class="pill">12+ months</span><h3 class="phase-name">Continuous Optimization</h3><p class="phase-text">Lorem ipsum dolor sit amet, consectetur adipiscing elit, sed do eiusmod tempor incididunt ut labore et dolore magna aliqua. Ut enim ad minim veniam, quis nostrud exercitation ullamcosint occaecat cupidatat non proident, sunt in culpa qui officia deserunt.</p></div>
</section>

<!-- Leadership -->
<section class="slide leaders">
  <div class="network" role="img" aria-label="Faint data network pattern"></div>
  <h2 class="slide-title" style="top:14px">Our <span class="accent">Leadership</span></h2>
  <div class="title-rule" style="top:42px;width:115px"></div>
  <article class="abs leader" style="left:9px"><div class="portrait" role="img" aria-label="Portrait photo of the CEO"></div><h3 class="leader-name">Dr. Owen Hale</h3><p class="leader-role">CEO, AI Strategy Expert</p><p class="leader-bio">Lorem ipsum dolor sit amet, consectetur adipiscing elit, sed do eiusmod tempor incididunt ut labore et dolore magna aliqua. Ut enim ad minim veniam, quis nostrud exercitation ullamco la boris nisi ut aliquip ex ea</p></article>
  <article class="abs leader" style="left:116px"><div class="portrait" role="img" aria-label="Portrait photo of the CTO"></div><h3 class="leader-name">Clara Mendes</h3><p class="leader-role">CTO, Automation Architect</p><p class="leader-bio">Lorem ipsum dolor sit amet, consectetur adipiscing elit, sed do eiusmod tempor incididunt ut labore et dolore magna aliqua. Ut enim ad minim veniam, quis nostrud exercitation ullamco la boris nisi ut aliquip ex ea</p></article>
  <article class="abs leader" style="left:224px"><div class="portrait" role="img" aria-label="Portrait photo of the head of data science"></div><h3 class="leader-name">Ravi Shah</h3><p class="leader-role">Head of Data Science</p><p class="leader-bio">Lorem ipsum dolor sit amet, consectetur adipiscing elit, sed do eiusmod tempor incididunt ut labore et dolore magna aliqua. Ut enim ad minim veniam, quis nostrud exercitation ullamco la boris nisi ut aliquip ex ea</p></article>
  <article class="abs leader" style="left:332px"><div class="portrait" role="img" aria-label="Portrait photo of the director"></div><h3 class="leader-name">Nina Park</h3><p class="leader-role">Director</p><p class="leader-bio">Lorem ipsum dolor sit amet, consectetur adipiscing elit, sed do eiusmod tempor incididunt ut labore et dolore magna aliqua. Ut enim ad minim veniam, quis nostrud exercitation ullamco la boris nisi ut aliquip ex ea</p></article>
</section>

<!-- Closing -->
<section class="slide dark closing">
  <div class="abs brand-lockup" style="top:33px">
    <div class="brand-name">FALCON REED INDUSTRIES</div>
    <div class="brand-tag">Engineering AI Transformations</div>
  </div>
  <h2 class="abs thanks">Thank You</h2>
  <p class="abs contact" style="top:170px">
    <svg width="11" height="8" viewBox="0 0 11 8"><rect x=".5" y=".5" width="10" height="7" fill="none" stroke="#fff" stroke-width=".9"/><path d="M.5 .5l5 4 5-4" fill="none" stroke="#fff" stroke-width=".9"/></svg>
    contact@falconreed.ai
  </p>
  <p class="abs contact" style="top:207px">
    <svg width="11" height="11" viewBox="0 0 12 12"><circle cx="6" cy="6" r="5.2" fill="none" stroke="#fff" stroke-width=".9"/><ellipse cx="6" cy="6" rx="2.3" ry="5.2" fill="none" stroke="#fff" stroke-width=".9"/><path d="M.8 6h10.4" stroke="#fff" stroke-width=".9"/></svg>
    www.falconreed.ai
  </p>
</section>

</body>
</html>
```